Web Design Project for NCYB

Hi,
I am looking for a website design for the Northern Council for Youth Boards.
This is an organisation which helps with legal disputes and other challenges which involve children.  The company want a web page which is professional but friendly.  The purpose of the website is to explain what the organisation does and to give people a place where they can download documents and information.
The homepage will have a video on the page.  ALSO, we would prefer the site to have a left hand navigation (not a top navigation).
I have enclosed the logo, a picture of the old (rubbish) home page and a screenshot from the video (you are welcome to change the dimensions).
If you have any questions, please ask.
-K
UPDATE: 6th DECEMBER:
Thanks for the designs so far.  I promise to give feedback to every single person.  In the meantime, can I just say that there's some good designs so far but I don't think anyone has nailed this yet.
So, I am uploading a screenshot called "theylikethis.jpg".  This is a screenshot from a website that the client says they like.
Can I also say, it's okay to reduce the size of the video.  I'm seeing a lot of massive videos.
Thanks folks!
UPDATE:  You can view a live demo of the site that they like at www.demohostqz.co.uk
UPDATE:  I've just found another good example of a site with a left nav at www.brightresourcehubnet.com

Hi,
Hi folks,
Had a quick look at the designs and just to say how impressed I am with the qualityand choice. There are a few that caught my eye and I'll try and narrow them down.I've also passed the link onto the other representatives for their input beforemaking a final choice. If I don't hear from any of the other represenatatives by Wednesday, I'll chose adesign and let you know. Once again many thanks for the quick response in gettingdesigns done and really looking forward to seeing the completed website.
Industry/Entity Type
Legal
Requirements
Must have
- a video player (any size of your choosing)
a left side navigation
the logo

```html
<!DOCTYPE html>
<html lang="en">
<head>
<meta charset="utf-8">
<title>Why Was The NCYB Formed? – Northern Council for Youth Boards</title>
<link rel="stylesheet" href="https://fonts.googleapis.com/css2?family=Arimo:wght@400;700&family=Oswald:wght@300;400;500&display=swap">
<style>
  :root {
    --page: #ffffff;
    --ink: #333333;
    --ink-soft: #555555;
    --brand-blue: #1d4f9c;
    --brand-deep: #163a78;
    --sky-light: #e6eefb;
    --sky-mid: #8fb0e6;
    --accent-red: #c0272d;
    --rule: #c8c8c8;
    --panel-bg: #f2f2f2;
    --footer-bg: #e9e9e9;
    --footer-ink: #777777;
    --link: #2b5aa8;
  }
  * { box-sizing: border-box; margin: 0; padding: 0; }
  html, body { width: 1200px; height: 1193px; overflow: hidden; background: var(--page); }
  body { position: relative; font-family: "Arimo", Arial, sans-serif; color: var(--ink); }

  .site-header {
    position: absolute; left: 0; top: 0; width: 1200px; height: 200px;
    background: linear-gradient(100deg, #ffffff 0%, var(--sky-light) 20%, var(--sky-mid) 45%, #3f6fc4 60%, var(--sky-light) 80%, #ffffff 100%);
  }
  .brand { position: absolute; left: 36px; top: 30px; display: flex; align-items: center; gap: 12px; }
  .brand-square { width: 44px; height: 44px; background: var(--brand-deep); }
  .brand-name { font-weight: 700; font-size: 34px; color: var(--brand-deep); letter-spacing: 1px; }

  .side-nav { position: absolute; left: 12px; top: 196px; width: 236px; }
  .side-nav ul { list-style: none; }
  .side-nav li { border-bottom: 1px solid var(--rule); height: 30px; line-height: 30px; font-size: 13px; }
  .side-nav a { color: var(--link); text-decoration: none; }

  .guide-promo {
    position: absolute; left: 12px; top: 538px; width: 236px;
    font-family: "Oswald", sans-serif; font-weight: 400; font-size: 35px; line-height: 41px;
    color: var(--brand-blue); text-transform: uppercase;
  }
  .social-row { position: absolute; left: 12px; top: 790px; display: flex; gap: 8px; }
  .social-row span { width: 26px; height: 26px; border-radius: 3px; }
  .guide-art {
    position: absolute; left: 12px; top: 826px; width: 170px; height: 222px;
    background: linear-gradient(180deg, #f7f3ec 0%, #f3e2a8 45%, #b9d98a 100%);
  }

  .main { position: absolute; left: 281px; top: 0; width: 895px; }
  .page-title {
    position: absolute; left: 0; top: 196px; width: 895px; padding-bottom: 8px;
    font-family: "Oswald", sans-serif; font-weight: 500; font-size: 31px; color: #2d2d2d;
    border-bottom: 1px solid var(--rule);
  }
  .intro { position: absolute; left: 0; top: 296px; width: 890px; font-size: 11.5px; line-height: 16px; color: var(--ink-soft); }

  .objectives-label { position: absolute; left: 0; top: 398px; font-size: 19px; font-weight: 700; color: var(--accent-red); letter-spacing: 0.5px; }
  .objectives-lead { position: absolute; left: 0; top: 438px; width: 530px; font-size: 23px; line-height: 28px; font-weight: 700; color: #3a3a3a; }
  .objectives-list { position: absolute; left: 30px; top: 574px; width: 500px; font-size: 11.5px; line-height: 17px; color: var(--ink-soft); }
  .objectives-list li { margin-bottom: 5px; padding-left: 6px; }
  .objectives-list li::marker { color: var(--accent-red); }

  .video-card { position: absolute; left: 559px; top: 380px; width: 328px; height: 376px; border: 1px solid var(--rule); background: var(--page); }
  .video-frame { position: absolute; left: 12px; top: 12px; width: 302px; height: 236px; background: linear-gradient(180deg, #f4f4f4 0%, #e8dcd2 55%, #d9c4b5 100%); }
  .video-play { position: absolute; left: 126px; top: 92px; }
  .video-title { position: absolute; left: 0; top: 262px; width: 100%; text-align: center; font-size: 17px; line-height: 20px; color: #3a3a3a; text-transform: uppercase; }
  .video-note { position: absolute; left: 14px; top: 314px; width: 300px; font-size: 11.5px; line-height: 15px; color: var(--ink-soft); }
  .video-note a { color: var(--link); }

  .members-title { position: absolute; left: 0; top: 786px; width: 895px; padding-bottom: 6px; font-size: 22px; font-weight: 700; color: #3a3a3a; border-bottom: 1px solid var(--rule); }
  .members-text { position: absolute; left: 0; top: 836px; width: 890px; font-size: 11.5px; line-height: 16px; color: var(--ink-soft); }

  .join-panel {
    position: absolute; left: 0; top: 932px; width: 895px; height: 118px;
    border: 1px solid var(--rule); background: linear-gradient(180deg, #fbfbfb 0%, var(--panel-bg) 100%);
    display: flex; align-items: center; justify-content: center;
    font-family: "Oswald", sans-serif; font-weight: 400; font-size: 33px; color: var(--link); text-transform: uppercase; text-decoration: none;
  }

  .site-footer { position: absolute; left: 0; top: 1073px; width: 1200px; height: 120px; background: var(--footer-bg); text-align: center; font-size: 11px; line-height: 15px; color: var(--footer-ink); }
  .site-footer a { color: var(--footer-ink); }
  .footer-links { padding-top: 26px; }
  .copyright { margin-top: 18px; }
</style>
</head>
<body>
  <header class="site-header">
    <div class="brand">
      <span class="brand-square"></span>
      <span class="brand-name">NCYB</span>
    </div>
  </header>

  <nav class="side-nav">
    <ul>
      <li><a href="#">Home</a></li>
      <li><a href="#">About NCYB</a></li>
      <li><a href="#">News</a></li>
      <li><a href="#">Conferences</a></li>
      <li><a href="#">Minutes</a></li>
      <li><a href="#">Annual Report</a></li>
      <li><a href="#">Archive</a></li>
      <li><a href="#">Contact Us</a></li>
      <li><a href="#">Links</a></li>
    </ul>
  </nav>

  <p class="guide-promo">A victim's guide to the youth board system.</p>
  <div class="social-row">
    <span style="background:#3b5998"></span>
    <span style="background:#41a6e0"></span>
    <span style="background:#5b8fd6"></span>
    <span style="background:#6ab04c"></span>
    <span style="background:#d34836"></span>
    <span style="background:#c4302b"></span>
  </div>
  <div class="guide-art" role="img" aria-label="Cartoon illustration of a young person with a reassuring message"></div>

  <main class="main">
    <h1 class="page-title">Why Was The NCYB Formed?</h1>
    <p class="intro">The NCYB was formed because it had been clear for a long time that the board members throughout the region needed to share in the development of the Youth Board System and to be able to communicate with one another through a recognised national body. A great deal of work and political support went into the set up of the NCYB. A national consultation took place and the Constitution of the Council was adopted at an inaugural meeting held in May 1977. More text here, and here, and some text here.</p>

    <h2 class="objectives-label">OBJECTIVES</h2>
    <p class="objectives-lead">Our Constitution states that our objectives are to promote the effectiveness of the Youth Board System by:</p>
    <ul class="objectives-list">
      <li>Providing a means of communication between youth board members, local, national and international bodies.</li>
      <li>Acting as a corporate voice for the views and needs of board members in all aspects of the Youth Board system.</li>
      <li>Providing a forum for the exchange of views and experiences.</li>
      <li>To promote a better understanding of the Youth Board System nationally and internationally.</li>
      <li>To organise events as appropriate to achieve any of the foregoing.</li>
    </ul>

    <aside class="video-card">
      <div class="video-frame" role="img" aria-label="Video still of a presenter explaining the youth board system">
        <svg class="video-play" width="50" height="50" viewBox="0 0 50 50" aria-hidden="true">
          <circle cx="25" cy="25" r="24" fill="rgba(0,0,0,0.35)"/>
          <path d="M20 15 L36 25 L20 35 Z" fill="#ffffff"/>
        </svg>
      </div>
      <p class="video-title">How does<br>the system work?</p>
      <p class="video-note"><a href="#">Watch</a> this short presentation which explains the development of the Youth Board system.</p>
    </aside>

    <h2 class="members-title">OUR MEMBERS</h2>
    <p class="members-text">Members include highly accomplished leaders from a large variety of industrial, financial, social and political sectors. This is an organisation which helps with legal disputes and other challenges which involve children. The company want a web page which is professional but friendly. The purpose of the website is to explain what the organisation does and to give people a place where they can download documents and information.</p>

    <a class="join-panel" href="#">Join the Youth Board</a>
  </main>

  <footer class="site-footer">
    <p class="footer-links"><a href="#">Home</a> | <a href="#">About NCYB</a> | <a href="#">Why Join</a> | <a href="#">Join Now</a> | <a href="#">Member Login</a> | <a href="#">Contact</a><br><a href="#">What We Offer</a> | <a href="#">Residential Links</a> | <a href="#">Become an Affiliate</a> | <a href="#">Course Information</a> | <a href="#">Member Benefits</a></p>
    <p class="copyright">Copyright © 2013 NCYB <a href="#">Terms of Use</a> | <a href="#">Privacy Policy</a> | <a href="#">Affiliate Agreement</a></p>
  </footer>
</body>
</html>
```